Stationary Design for Stunning new Logo

I need to envelopes, letterhead, business cards designed to compliment our new logo.

We are a 25 year old printing company going through a brand refresh. All items should have the design extended to both sides for full print ability.

Industry/Entity Type

Printing

Requirements
Must have
• It must utilize the new logo & colors PMS 300 & PMS 295.

```html
<!DOCTYPE html>
<html lang="en">
<head>
<meta charset="utf-8">
<title>Northmark Stationery Set</title>
<link href="https://fonts.googleapis.com/css2?family=PT+Sans+Narrow:wght@400;700&family=Didact+Gothic&display=swap" rel="stylesheet">
<style>
  :root {
    --pms-300: #0a5fc4;
    --pms-295: #0a3a86;
    --band-dark: #0a2fb0;
    --band-light: #3d93f2;
    --ink: #2a2a2a;
    --paper: #ffffff;
    --board: #b9bdc1;
  }
  * { margin: 0; padding: 0; box-sizing: border-box; }
  html, body { width: 1200px; height: 848px; overflow: hidden; }
  body {
    position: relative;
    background: var(--board);
    font-family: "PT Sans Narrow", "Arial Narrow", sans-serif;
    color: var(--ink);
  }
  .piece {
    position: absolute;
    background: var(--paper);
    box-shadow: 3px 4px 6px rgba(0,0,0,.35);
    overflow: hidden;
  }
  .band {
    position: absolute; left: 0; right: 0;
    background: linear-gradient(90deg, var(--band-dark) 0%, var(--band-light) 45%, var(--band-dark) 60%, var(--band-light) 85%, var(--band-dark) 100%);
  }
  .band-top { top: 0; }
  .band-bottom { bottom: 0; }

  .brand {
    position: absolute;
    display: flex; align-items: center; gap: 4px;
    font-family: "PT Sans Narrow", sans-serif;
    font-weight: 700;
    color: var(--pms-300);
    letter-spacing: .5px;
    line-height: 1;
  }
  .brand-dot { border-radius: 50%; background: var(--pms-300); flex: none; }
  .lbl { font-weight: 700; color: var(--pms-300); }
  .web { font-weight: 700; color: var(--pms-300); }
  .dot-mark { position: absolute; border-radius: 50%; background: var(--pms-300); }

  /* Letterhead */
  .letterhead { left: 25px; top: 35px; width: 547px; height: 773px; }
  .letterhead .band-top { height: 7px; }
  .letterhead .band-bottom { height: 10px; }
  .letterhead .brand { right: 27px; top: 18px; font-size: 21px; }
  .letterhead .brand-dot { width: 16px; height: 16px; }
  .lh-footer { position: absolute; top: 694px; font-size: 10px; line-height: 11.2px; }
  .lh-footer .body { font-family: "Didact Gothic", sans-serif; color: #444; }
  .lh-office { left: 26px; }
  .lh-mail { left: 201px; }
  .lh-phone { left: 384px; }
  .letterhead .web { position: absolute; left: 384px; top: 738px; font-size: 10.5px; }
  .letterhead .dot-mark { left: 480px; top: 700px; width: 38px; height: 38px; }

  /* Cards */
  .card { width: 255px; height: 155px; font-size: 9px; line-height: 11.5px; }
  .card .band { height: 7px; }
  .card .brand { font-size: 16px; }
  .card .brand-dot { width: 12px; height: 12px; }
  .card-person { left: 623px; top: 35px; }
  .card-person .brand { right: 22px; top: 18px; }
  .card-person .name { position: absolute; right: 64px; top: 51px; font-family: "Didact Gothic", sans-serif; font-size: 18px; color: #222; }
  .card-person .role { position: absolute; right: 64px; top: 72px; font-family: "Didact Gothic", sans-serif; font-size: 10px; font-style: italic; color: #333; }
  .card-person .contacts { position: absolute; right: 26px; top: 113px; text-align: right; }
  .card-address { left: 893px; top: 35px; height: 153px; }
  .card-address .brand { left: 20px; top: 18px; }
  .card-address .contacts { position: absolute; left: 28px; top: 67px; font-size: 8.5px; line-height: 11.3px; }
  .card-address .web { position: absolute; left: 128px; top: 122px; font-size: 10px; }
  .card-address .dot-mark { left: 218px; top: 110px; width: 26px; height: 26px; }
  .card-office { left: 623px; top: 215px; height: 157px; }
  .card-office .brand, .card-mail .brand { left: 50%; transform: translateX(-50%); top: 30px; }
  .card-office .contacts { position: absolute; left: 9px; top: 103px; line-height: 12.2px; }
  .card-mail { left: 892px; top: 215px; width: 254px; height: 157px; }
  .card-mail .contacts { position: absolute; left: 14px; top: 103px; line-height: 12.2px; }
  .card-mail .dot-mark { left: 220px; top: 112px; width: 24px; height: 24px; }

  /* Envelopes */
  .env-front { left: 600px; top: 397px; width: 542px; height: 270px; }
  .env-front .band-bottom { height: 10px; }
  .env-front .brand { left: 14px; top: 21px; font-size: 18px; }
  .env-front .brand-dot { width: 14px; height: 14px; }
  .env-front .return { position: absolute; left: 31px; top: 43px; font-weight: 700; font-size: 10.5px; line-height: 12px; color: #333; }
  .env-back { left: 624px; top: 532px; width: 546px; height: 273px; }
  .env-back svg { position: absolute; left: 0; top: 0; }
  .env-back .band-bottom { height: 10px; }
  .env-back .web { position: absolute; left: 0; right: 0; top: 62px; text-align: center; color: #fff; font-size: 9.5px; }
</style>
</head>
<body>

<section class="piece letterhead">
  <div class="band band-top"></div>
  <div class="brand"><span class="brand-dot"></span>NORTHMARK</div>
  <div class="lh-footer lh-office">
    <div><span class="lbl">OFFICE</span> <span class="body">Northmark, Inc. 1275</span></div>
    <div class="body">Alder Industrial Drive</div>
    <div class="body">Brookfield, GA 30512</div>
    <div class="lbl">POSTAL ADDRESS <span class="body">Northmark, Inc.</span></div>
    <div class="body">POB 412 Brookfield, GA 30514</div>
  </div>
  <div class="lh-footer lh-mail">
    <div><span class="lbl">Sales</span> <span class="body">sales@northmark.us</span></div>
    <div><span class="lbl">Customer Service</span> <span class="body">service@northmark.us</span></div>
    <div><span class="lbl">Orders</span> <span class="body">orders@northmark.us</span></div>
    <div><span class="lbl">Art</span> <span class="body">art@northmark.us</span></div>
    <div><span class="lbl">Shipping</span> <span class="body">shipping@northmark.us</span></div>
  </div>
  <div class="lh-footer lh-phone">
    <div><span class="lbl">Free T</span> <span class="body">800.555.0142</span></div>
    <div><span class="lbl">Local T</span> <span class="body">770.555.0143</span></div>
    <div><span class="lbl">Fax</span> <span class="body">770.555.0144</span></div>
  </div>
  <div class="web">www.northmark-inc.com</div>
  <div class="dot-mark"></div>
  <div class="band band-bottom"></div>
</section>

<section class="piece card card-person">
  <div class="brand"><span class="brand-dot"></span>NORTHMARK</div>
  <div class="name">Project Owner</div>
  <div class="role">diretor</div>
  <div class="contacts">
    <div><span class="lbl">M</span> 800.000.0000 <span class="lbl">E</span> xxxx@northmark.us</div>
    <div><span class="lbl">Free T</span> 800.555.0142 <span class="lbl">Local T</span> 770.555.0143 <span class="lbl">Fax</span> 770.555.0144</div>
  </div>
  <div class="band band-bottom"></div>
</section>

<section class="piece card card-address">
  <div class="brand"><span class="brand-dot"></span>NORTHMARK</div>
  <div class="contacts">
    <div><span class="lbl">OFFICE</span> Northmark, Inc. 1275</div>
    <div>Alder Industrial Drive</div>
    <div>Brookfield, GA 30512</div>
    <div><span class="lbl">POSTAL ADDRESS</span> Northmark, Inc.</div>
    <div>POB 412 Brookfield, GA 30514</div>
  </div>
  <div class="web">www.northmark-inc.com</div>
  <div class="dot-mark"></div>
  <div class="band band-bottom"></div>
</section>

<section class="piece card card-office">
  <div class="band band-top"></div>
  <div class="brand"><span class="brand-dot"></span>NORTHMARK</div>
  <div class="contacts">
    <div><span class="lbl">OFFICE</span> Northmark, Inc. 1275 Alder Industrial Drive, Brookfield, GA 30512</div>
    <div><span class="lbl">POSTAL ADDRESS</span> Northmark, Inc. POB 412 Brookfield, GA 30514</div>
    <div><span class="lbl">Free T</span> 800.555.0142 <span class="lbl">Local T</span> 770.555.0143 <span class="lbl">Fax</span> 770.555.0144</div>
  </div>
  <div class="band band-bottom"></div>
</section>

<section class="piece card card-mail">
  <div class="band band-top"></div>
  <div class="brand"><span class="brand-dot"></span>NORTHMARK</div>
  <div class="contacts">
    <div><span class="lbl">Sales</span> sales@northmark.us <span class="lbl">Customer Service</span> service@northmark.us</div>
    <div><span class="lbl">Orders</span> orders@northmark.us <span class="lbl">Art</span> art@northmark.us</div>
    <div><span class="lbl">Shipping</span> shipping@northmark.us <span class="web">www.northmark-inc.com</span></div>
  </div>
  <div class="dot-mark"></div>
  <div class="band band-bottom"></div>
</section>

<section class="piece env-front">
  <div class="brand"><span class="brand-dot"></span>NORTHMARK</div>
  <div class="return">
    <div>Northmark, Inc. 1275</div>
    <div>Alder Industrial Drive</div>
    <div>Brookfield, GA 30512</div>
  </div>
  <div class="band band-bottom"></div>
</section>

<section class="piece env-back">
  <svg width="546" height="273" viewBox="0 0 546 273" aria-hidden="true">
    <path d="M0 0 H546 L300 96 Q273 104 246 96 Z" fill="var(--pms-295)"/>
  </svg>
  <div class="web">www.northmark-inc.com</div>
  <div class="band band-bottom"></div>
</section>

</body>
</html>
```